Manufacturing company needs new business card.

I need a unique Business Card that will truly stand out. Nothing too busy. Simple is good, right? Not looking for a standard design either. No cookie cutter layout. I am just looking for something interesting and a bit different. Does't have to completely off the wall crazy, just not your run of the mill business card. Clean and modern with a touch of industrial.

Target Market(s)

Air conditioning industry, Architects, builders.

Industry/Entity Type

Business

Contact Information for Business Card

Details to be included on card are:

Peter Vance
Managing Director

T: 1300 847 519
M: 0428 593 174
W: www.brenvaleworks.com.au
E: peter.vance@brenvaleworks.com.au
A: 58 Harwick Lane, Sydney NSW 2000

Font styles to use
Sans Serif

Colors
0355a3
848484
fbfbfb

Requirements
Must have
• Card design must be landscape.

```html
<!DOCTYPE html>
<html lang="en">
<head>
<meta charset="utf-8">
<title>Brenvale Works – Business Card</title>
<link rel="stylesheet" href="https://fonts.googleapis.com/css2?family=Open+Sans:wght@300;400;600;700&display=swap">
<style>
  :root {
    --brand-blue: #0355a3;
    --brand-grey: #848484;
    --card-white: #fbfbfb;
    --band-grey: #eeeeee;
    --ink-dark: #2b2b2b;
    --ink-body: #3a3a3a;
    --backdrop: #262626;
  }
  * { box-sizing: border-box; margin: 0; padding: 0; }
  html, body { width: 1200px; height: 1000px; overflow: hidden; }
  body {
    background: var(--backdrop);
    font-family: "Open Sans", Arial, sans-serif;
    position: relative;
  }
  .card {
    position: absolute;
    width: 560px;
    height: 342px;
    background: var(--card-white);
    border-radius: 28px;
    overflow: hidden;
  }
  .card--back { left: 70px; top: 110px; }
  .card--front { left: 570px; top: 540px; }

  /* brand name lockup */
  .brand {
    position: absolute;
    display: flex;
    align-items: center;
    gap: 14px;
  }
  .brand__square {
    width: 34px; height: 34px;
    background: var(--brand-blue);
    border-radius: 3px;
  }
  .brand__name {
    color: var(--brand-blue);
    font-weight: 600;
    font-size: 28px;
    letter-spacing: -0.3px;
    white-space: nowrap;
  }

  /* back side */
  .card--back .brand { left: 40px; bottom: 48px; }
  .back__band {
    position: absolute;
    right: 0; bottom: 0;
    width: 250px; height: 150px;
    background: var(--band-grey);
    clip-path: polygon(22% 0, 100% 0, 100% 100%, 0 100%);
  }
  .back__web {
    position: absolute;
    right: 34px; bottom: 120px;
    font-size: 12.5px;
    color: var(--ink-body);
  }

  /* front side */
  .front__person {
    position: absolute;
    right: 170px; top: 34px;
    text-align: right;
  }
  .front__name {
    font-size: 26px;
    letter-spacing: 0.5px;
    line-height: 1;
    color: var(--ink-dark);
    font-weight: 600;
  }
  .front__name span { font-weight: 300; color: var(--brand-grey); }
  .front__title {
    display: inline-block;
    margin-top: 6px;
    padding: 3px 9px;
    background: var(--brand-blue);
    color: #fff;
    font-size: 10.5px;
    letter-spacing: 1px;
    text-transform: uppercase;
  }
  .front__mark {
    position: absolute;
    right: 30px; top: 40px;
    width: 118px; height: 118px;
    background: var(--brand-blue);
    border-radius: 10px;
  }
  .card--front .brand { left: 40px; top: 150px; }
  .front__rule {
    position: absolute;
    left: 0; right: 0; top: 222px;
    height: 3px;
    background: var(--brand-blue);
  }
  .front__band {
    position: absolute;
    left: 0; right: 0; top: 225px; bottom: 0;
    background: var(--band-grey);
  }
  .contacts {
    position: absolute;
    left: 40px; right: 30px; top: 196px;
    font-size: 13px;
    color: var(--ink-body);
  }
  .contact {
    display: flex;
    align-items: center;
    gap: 8px;
    line-height: 20px;
  }
  .contact svg { width: 13px; height: 13px; fill: var(--brand-blue); flex: none; }
  .contacts__address { margin-bottom: 18px; }
  .contacts__grid {
    display: grid;
    grid-template-columns: 170px 1fr;
    row-gap: 4px;
  }
</style>
</head>
<body>

<section class="card card--back" aria-label="Business card back">
  <div class="back__band"></div>
  <p class="back__web">www.brenvaleworks.com.au</p>
  <div class="brand">
    <div class="brand__square"></div>
    <span class="brand__name">Brenvale Works</span>
  </div>
</section>

<section class="card card--front" aria-label="Business card front">
  <div class="front__band"></div>
  <div class="front__rule"></div>
  <div class="front__mark"></div>
  <div class="front__person">
    <p class="front__name">PETER <span>VANCE</span></p>
    <p class="front__title">Managing Director</p>
  </div>
  <div class="brand">
    <div class="brand__square"></div>
    <span class="brand__name">Brenvale Works</span>
  </div>

  <div class="contacts">
    <p class="contact contacts__address">
      <svg viewBox="0 0 16 16" aria-hidden="true"><path d="M8 1 1 7.5h2V15h4v-4.5h2V15h4V7.5h2z"/></svg>
      58 Harwick Lane, Sydney NSW 2000
    </p>
    <div class="contacts__grid">
      <p class="contact">
        <svg viewBox="0 0 16 16" aria-hidden="true"><path d="M2 5c0-2 2-3 6-3s6 1 6 3v1h-3V4.5H5V6H2zM4 7h8l2 7H2z"/></svg>
        1300 847 519
      </p>
      <p class="contact">
        <svg viewBox="0 0 16 16" aria-hidden="true"><path d="M1 3h14v10H1zm1.5 1.5L8 9l5.5-4.5"/></svg>
        peter.vance@brenvaleworks.com.au
      </p>
      <p class="contact">
        <svg viewBox="0 0 16 16" aria-hidden="true"><path d="M3 1.5 6 1l1.5 4L5.5 6.5a9 9 0 0 0 4 4L11 8.5l4 1.5-.5 3c-.3 1.5-2 2-3.5 1.5A14 14 0 0 1 1.5 5C1 3.5 1.5 1.8 3 1.5z"/></svg>
        0428 593 174
      </p>
      <p class="contact">
        <svg viewBox="0 0 16 16" aria-hidden="true"><circle cx="8" cy="8" r="7"/></svg>
        www.brenvaleworks.com.au
      </p>
    </div>
  </div>
</section>

</body>
</html>
```